PressLeaf Design Project

NOTICE TO DESIGNERS
****************NOTE: PLEASE DO NOT SUBMIT ANY MORE DESIGNS, THANK YOU!!!!****************
The name of our business is Harbor Pixel Guild and we are setting up a website to review new phones/tablets in the marketplace.
We require a 5 page design, the idea behind the project can be understood better if you visit this websites
1) tallowbrook.example
2) http://vrnqo.example/reviews/cellphones/
Pages required are;
1) Home page which lists all the current top devices
2) A single device page that shows the device with its current specs
3) Comparison page - where 2 or 3 devices are being compared in terms of specs
4) Archive page that shows all the current videos and text reviews
5) Single post page for the device being reviewed with all its pictures, written review, video with sidebar on the side showing other reviews available.
I am opened to a nice color scheme, including red, blue and orange. We do not have any logo at the moment. Thanks
This is a notice to all designers, I have found the designer I want to work with please do not submit any more designs for now. Thank you

```html
<!DOCTYPE html>
<html lang="en">
<head>
<meta charset="utf-8">
<title>Harbor Pixel Guild – Phones</title>
<link rel="stylesheet" href="https://fonts.googleapis.com/css2?family=Josefin+Sans:wght@600;700&family=Open+Sans:wght@400;600&family=Montserrat:wght@700&display=swap">
<style>
  :root {
    --page-bg: #efefef;
    --panel: #ffffff;
    --brand-yellow: #fbb900;
    --ink: #1e1e1e;
    --ink-soft: #555555;
    --ink-muted: #777777;
    --accent-orange: #f07b1e;
    --topbar: #2d2d2d;
    --line: #e2e2e2;
    --pager-bg: #e4e4e4;
    --hero-a: #f4f4f4;
    --hero-b: #d9d9d9;
  }
  * { box-sizing: border-box; margin: 0; padding: 0; }
  html, body { width: 1200px; height: 482px; overflow: hidden; }
  body {
    position: relative;
    background: var(--page-bg);
    font-family: "Open Sans", Arial, sans-serif;
    color: var(--ink);
  }
  .top-rule { position: absolute; left: 0; top: 0; width: 1200px; height: 3px; background: var(--topbar); }
  .cart {
    position: absolute; left: 902px; top: 0; width: 120px; height: 26px;
    background: var(--topbar); color: #fff;
    font: 400 11px/26px Arial, sans-serif; padding-left: 17px;
  }
  .cart svg { position: absolute; right: 16px; top: 11px; }

  .brand {
    position: absolute; left: 178px; top: 30px;
    font-family: "Montserrat", sans-serif; font-weight: 700;
    font-size: 27px; line-height: 30px; letter-spacing: 0.5px;
    color: var(--ink); text-transform: uppercase;
  }

  .search { position: absolute; left: 550px; top: 40px; display: flex; gap: 6px; }
  .search-field {
    width: 202px; height: 26px; background: var(--panel);
    font-size: 9px; color: var(--ink-muted); line-height: 26px; padding-left: 10px;
  }
  .search-button { width: 62px; height: 26px; background: #dcdcdc; display: flex; align-items: center; justify-content: center; }

  .welcome { position: absolute; right: 179px; top: 39px; font: 400 9.5px Arial, sans-serif; color: var(--ink-soft); }
  .account { position: absolute; right: 179px; top: 60px; display: flex; font: 400 11px Arial, sans-serif; }
  .account a { color: var(--ink); text-decoration: none; }
  .account a + a { border-left: 1px solid #ccc; margin-left: 9px; padding-left: 9px; }

  .main-nav {
    position: absolute; left: 178px; top: 101px; width: 844px; height: 40px;
    background: var(--brand-yellow);
  }
  .main-nav a, .buy-item {
    position: absolute; top: 0; line-height: 42px;
    font-family: "Josefin Sans", sans-serif; font-weight: 700; font-size: 15px;
    color: #fff; text-decoration: none; white-space: nowrap;
  }
  .buy-item { left: 1067px; top: 101px; color: #fafafa; }

  .breadcrumbs {
    position: absolute; left: 178px; top: 155px; width: 844px; height: 22px;
    background: var(--panel); font-size: 9.5px; color: var(--ink-soft);
    line-height: 22px;
  }
  .breadcrumbs span { position: absolute; top: 0; }
  .back-link { position: absolute; right: 10px; top: 0; }

  .sidebar {
    position: absolute; left: 178px; top: 191px; width: 189px; height: 300px;
    background: var(--panel);
  }
  .sidebar-title {
    height: 48px; border-bottom: 1px solid var(--line);
    font-family: "Josefin Sans", sans-serif; font-weight: 700; font-size: 23px;
    text-align: center; line-height: 55px; letter-spacing: 1px;
  }
  .category-list { list-style: none; padding-top: 13px; font-size: 9.5px; }
  .category-list li { line-height: 15.8px; }
  .cat-root { color: var(--accent-orange); padding-left: 32px; font-size: 11px; position: relative; }
  .cat-root svg { position: absolute; left: 18px; top: 6px; }
  .cat-brand { padding-left: 32px; color: var(--ink); font-size: 9.5px; }
  .cat-item { padding-left: 42px; color: var(--ink-soft); font-size: 9px; }

  .hero {
    position: absolute; left: 385px; top: 191px; width: 637px; height: 236px;
    background: linear-gradient(160deg, var(--hero-a) 0%, #e8e8e8 55%, var(--hero-b) 100%);
  }
  .listing-bar {
    position: absolute; left: 385px; top: 427px; width: 637px; height: 41px;
    background: var(--panel); border-bottom: 1px solid #cfcfcf;
  }
  .item-count {
    position: absolute; left: 18px; top: 0; line-height: 41px;
    font: 400 11px Arial, sans-serif; color: var(--ink-soft);
  }
  .pager { position: absolute; left: 445px; top: 10px; display: flex; align-items: center; gap: 4px; }
  .pager-label { font: 400 11px Arial, sans-serif; color: var(--ink-soft); margin-right: 9px; }
  .page {
    width: 23px; height: 22px; background: var(--pager-bg);
    font: 400 11px/22px Arial, sans-serif; text-align: center; color: var(--ink-soft);
  }
  .page.current { background: var(--brand-yellow); color: #fff; }
  .page.first { background: #d6d6d6; }
  .page.next { background: #ececec; display: flex; align-items: center; justify-content: center; }
  .lower-panel { position: absolute; left: 385px; top: 469px; width: 637px; height: 20px; background: var(--panel); }
</style>
</head>
<body>
  <div class="top-rule"></div>
  <div class="cart">CART - £0.00
    <svg width="8" height="5" viewBox="0 0 8 5"><path d="M0 0h8L4 5z" fill="#fff"/></svg>
  </div>

  <div class="brand">Harbor Pixel<br>Guild</div>

  <div class="search">
    <div class="search-field">Search entire store here...</div>
    <div class="search-button">
      <svg width="16" height="14" viewBox="0 0 16 14"><circle cx="6" cy="5.5" r="4" fill="none" stroke="#444" stroke-width="1.8"/><path d="M9 8.5l5 4" stroke="#444" stroke-width="2.2" stroke-linecap="round"/></svg>
    </div>
  </div>

  <div class="welcome">Welcome to our PressLeaf store</div>
  <div class="account"><a href="#">Register</a><a href="#">Sign In</a></div>

  <nav class="main-nav">
    <a href="#" style="left:17px">Home</a>
    <a href="#" style="left:90px">Top Phones</a>
    <a href="#" style="left:202px">Gadgets</a>
    <a href="#" style="left:294px">Latest Phones</a>
    <a href="#" style="left:421px">Appliances</a>
    <a href="#" style="left:536px">Custom Block</a>
    <a href="#" style="left:667px">Custom Block 2</a>
  </nav>
  <div class="buy-item">Buy Item</div>

  <div class="breadcrumbs">
    <span style="left:10px">Home &nbsp;→</span>
    <span style="left:69px">Women &nbsp;→</span>
    <span style="left:136px">Accessories</span>
    <span class="back-link">
      <svg width="5" height="7" viewBox="0 0 5 7"><path d="M5 0v7L0 3.5z" fill="#333"/></svg>
      &nbsp;&nbsp;Back to previous page
    </span>
  </div>

  <aside class="sidebar">
    <h2 class="sidebar-title">PHONES</h2>
    <ul class="category-list">
      <li class="cat-root"><svg width="8" height="5" viewBox="0 0 8 5"><path d="M0 2.5h7M5 0.5l2 2-2 2" fill="none" stroke="#f07b1e" stroke-width="0.8"/></svg>Phones</li>
      <li class="cat-brand">Orchard</li>
      <li class="cat-item">Halo</li>
      <li class="cat-item">Halo4</li>
      <li class="cat-item">Halo4S</li>
      <li class="cat-item">Halo5</li>
      <li class="cat-item">Halo6</li>
      <li class="cat-brand">Nordvik</li>
      <li class="cat-item">Cold Weather</li>
      <li class="cat-item">Bags and Wallets</li>
      <li class="cat-item">Belts</li>
      <li class="cat-item">Jewelry</li>
      <li class="cat-item">Ties and Hats</li>
      <li class="cat-item">Socks</li>
      <li class="cat-item">Sunglasses</li>
    </ul>
  </aside>

  <div class="hero" role="img" aria-label="Category banner: grey paper mockup with outline sketches of phones and tablets"></div>

  <div class="listing-bar">
    <div class="item-count">THERE ARE 195 ITEMS ON 17 PAGES</div>
    <div class="pager">
      <span class="pager-label">PAGE:</span>
      <span class="page first">1</span>
      <span class="page">2</span>
      <span class="page current">3</span>
      <span class="page">4</span>
      <span class="page next"><svg width="5" height="7" viewBox="0 0 5 7"><path d="M0 0v7l5-3.5z" fill="#333"/></svg></span>
    </div>
  </div>
  <div class="lower-panel"></div>
</body>
</html>
```